Business card and stationery for School
Business card and stationery for School - Education
Creative Brief
Use same font as used in my logo
However variations is permitted
Bright & Fun-filled
Mrs Belinda T. Marrowfield
Proprietress
Plot 418C QX4 Temberlo Layout Opposite Pinwick Office Halverton Road, Dosumi FCT, Abuja
info@bluepebbleacademy.example
www.bluepebbleacademy.example

```html
<!DOCTYPE html>
<html lang="en">
<head>
<meta charset="utf-8">
<title>Blue Pebble Academy – Business Card</title>
<link href="https://fonts.googleapis.com/css2?family=Cinzel:wght@400;600&family=Open+Sans:wght@400;600&display=swap" rel="stylesheet">
<style>
  :root {
    --backdrop: #e9e6e1;
    --card: #ffffff;
    --purple: #7a2a82;
    --purple-dark: #5e1d66;
    --green: #7ab43a;
    --grey-text: #555555;
    --dark-text: #333333;
    --grey-line: #c9c9c9;
  }
  * { margin: 0; padding: 0; box-sizing: border-box; }
  html, body { width: 1200px; height: 902px; overflow: hidden; background: var(--backdrop); }
  .card {
    position: absolute; left: 100px; top: 161px; width: 1000px; height: 580px;
    background: var(--card); overflow: hidden;
    box-shadow: 0 10px 30px rgba(0,0,0,.18);
  }
  .brand { position: absolute; top: 70px; left: 0; width: 100%; text-align: center; }
  .brand-mark {
    display: inline-block; width: 54px; height: 54px; border-radius: 50%;
    background: var(--purple); vertical-align: middle; margin-right: 14px;
  }
  .brand-name {
    display: inline-block; vertical-align: middle;
    font-family: "Cinzel", serif; font-weight: 600; font-size: 50px;
    color: var(--purple); letter-spacing: 1px;
  }
  .tagline-row {
    position: absolute; top: 150px; left: 0; width: 100%;
    display: flex; justify-content: center; align-items: center; gap: 30px;
  }
  .tagline { font-family: "Open Sans", sans-serif; font-size: 22px; color: var(--dark-text); }
  .accent-line { width: 170px; height: 4px; background: var(--green); }
  .holder { position: absolute; top: 218px; left: 0; width: 100%; text-align: center; }
  .holder-name { font-family: "Cinzel", serif; font-weight: 600; font-size: 27px; color: var(--purple); }
  .holder-title { font-family: "Cinzel", serif; font-weight: 400; font-size: 18px; color: var(--grey-text); margin-top: 4px; }
  .contacts {
    position: absolute; top: 310px; left: 40px; right: 40px;
    font-family: "Open Sans", sans-serif; font-size: 14px; color: var(--grey-text);
  }
  .contact-row { display: flex; align-items: center; gap: 18px; margin-bottom: 12px; }
  .contact-item { display: flex; align-items: center; gap: 7px; white-space: nowrap; }
  .icon { width: 20px; height: 20px; flex: none; }
  .rule { position: absolute; top: 425px; left: 0; width: 560px; height: 3px; background: var(--grey-line); }
  .web-tab {
    position: absolute; top: 395px; left: 560px; right: 0; height: 75px;
    background: linear-gradient(var(--purple), var(--purple-dark));
    display: flex; align-items: center; justify-content: center;
    font-family: "Open Sans", sans-serif; font-size: 13px; letter-spacing: 3px;
    color: #fff; text-transform: uppercase; white-space: nowrap;
  }
  .base-band { position: absolute; bottom: 0; left: 0; width: 100%; height: 110px; background: var(--green); }
</style>
</head>
<body>
<div class="card">
  <div class="brand"><span class="brand-mark"></span><span class="brand-name">BLUE PEBBLE ACADEMY</span></div>
  <div class="tagline-row">
    <span class="tagline">Curious minds, bright futures</span>
    <span class="accent-line"></span>
  </div>

  <div class="holder">
    <div class="holder-name">MRS BELINDA T. MARROWFIELD</div>
    <div class="holder-title">PROPRIETRESS</div>
  </div>

  <div class="contacts">
    <div class="contact-row">
      <span class="contact-item">
        <svg class="icon" viewBox="0 0 20 20"><circle cx="10" cy="10" r="10" fill="var(--purple)"/><path d="M10 4.5a3.5 3.5 0 0 0-3.5 3.5c0 2.6 3.5 7 3.5 7s3.5-4.4 3.5-7A3.5 3.5 0 0 0 10 4.5zm0 5a1.4 1.4 0 1 1 0-2.8 1.4 1.4 0 0 1 0 2.8z" fill="#fff"/></svg>
        Plot 418C QX4 Temberlo Layout Opposite Pinwick Office Halverton Road, Dosumi FCT, Abuja
      </span>
    </div>
    <div class="contact-row">
      <span class="contact-item">
        <svg class="icon" viewBox="0 0 20 20"><circle cx="10" cy="10" r="10" fill="var(--purple)"/><path d="M7 5l2 2.5-1.2 1.3a6 6 0 0 0 3.4 3.4L12.5 11l2.5 2-1.2 1.8C9.5 15 5 10.5 5.2 6.2z" fill="#fff"/></svg>
        +234 (09) 555 0142
      </span>
      <span class="contact-item">
        <svg class="icon" viewBox="0 0 20 20"><circle cx="10" cy="10" r="10" fill="var(--purple)"/><rect x="7" y="4.5" width="6" height="11" rx="1" fill="#fff"/></svg>
        +234 800 555 0199
      </span>
      <span class="contact-item">
        <svg class="icon" viewBox="0 0 20 20"><circle cx="10" cy="10" r="10" fill="var(--purple)"/><rect x="5" y="6.5" width="10" height="7" fill="#fff"/><path d="M5 6.5l5 4 5-4" stroke="var(--purple)" stroke-width="1" fill="none"/></svg>
        info@bluepebbleacademy.example
      </span>
      <span class="contact-item">
        <svg class="icon" viewBox="0 0 20 20"><circle cx="10" cy="10" r="10" fill="var(--purple)"/><circle cx="10" cy="10" r="5" stroke="#fff" stroke-width="1.3" fill="none"/><path d="M5 10h10M10 5c-2.5 3-2.5 7 0 10M10 5c2.5 3 2.5 7 0 10" stroke="#fff" stroke-width="1" fill="none"/></svg>
        www.bluepebbleacademy.example
      </span>
    </div>
  </div>

  <div class="rule"></div>
  <div class="web-tab">www.bluepebbleacademy.example</div>
  <div class="base-band"></div>
</div>
</body>
</html>
```